Online Marketing Website

Create a website design for an online marketing company.

It should use modern designs:

Power of space,
Graphics supported content - less words more meaning
Grid and flow layout for listing type content
Provision for responsive and interactive CSS

http://www.brightkettlemedia.com.au/ is a very quick mock up, however this should only be used as an example and is not a indication of desired design. Examples that differ from this will be considered.
Updates

To all the developers who have submitted a design, There are a lot a great designs there. I am going to wait a little while longer before providing any feedback as I do not like wasting your time, and experience has shown good designs come late.

At this stage no news is not bad news... It is just that.

Thanks heaps for your work, will contact the leaders soon.

Target Market(s)

Small to Medium Business operating in the B2B or professional B2C space

Industry/Entity Type

Marketing

Requirements
Must have
• It should use a modern Panel design for the front page that will give a high level overview of the products with in-depth content pages for each service.

Nice to have
• Rotating banner at the top of the pages, no higher than 300px

Appropriate use of power colours such as red and Orange.
Should not have
• No Sidebars except on Post pages

```html
<!DOCTYPE html>
<html lang="en">
<head>
<meta charset="utf-8">
<title>Bright Kettle Media – Online Strategic Planning</title>
<link rel="stylesheet" href="https://fonts.googleapis.com/css2?family=Cabin:wght@400;500;600&family=Arimo:wght@400;700&display=swap">
<style>
:root{
  --orange:#f47b20;
  --orange-dark:#e0571e;
  --red:#c8262e;
  --ink:#2b2b2b;
  --muted:#555;
  --page-bg:#e9e9e9;
  --panel:#f3f3f3;
  --white:#ffffff;
  --bar-rest:#454545;
  --green:#3cb54a;
  --blue:#5b7fc4;
  --sky:#8ab4e8;
  --chart:#9fd0e8;
  --footer:#1e1e1e;
  --footer-strip:#2e2e2e;
}
*{box-sizing:border-box;margin:0;padding:0}
html,body{width:720px;height:1200px;overflow:hidden}
body{background:var(--page-bg);font-family:"Cabin",sans-serif;color:var(--ink);position:relative}
.page{position:absolute;left:60px;top:30px;width:600px;height:1134px;background:var(--white);border-top:3px solid var(--orange);overflow:hidden}
.section{position:absolute;left:0;width:600px}

/* top bar */
.topbar{top:0;height:20px;background:#f7f7f7;border-bottom:1px solid #e2e2e2;font-size:6.5px;color:#333}
.topbar .phone{position:absolute;left:16px;top:7px;display:flex;align-items:center;gap:5px}
.topbar .chat{position:absolute;left:93px;top:7px}
.login{position:absolute;right:0;top:0;width:44px;height:10px;background:var(--orange);color:#fff;font-size:6px;text-align:center;line-height:10px}

/* header */
.header{top:20px;height:38px;border-bottom:2px solid var(--red)}
.brand{position:absolute;left:16px;top:12px;display:flex;align-items:center;gap:6px}
.brand-mark{width:14px;height:14px;background:var(--red)}
.brand-name{font-size:10px;font-weight:600;color:var(--red);letter-spacing:.2px}
.nav{position:absolute;right:14px;top:15px;display:flex;gap:16px;font-size:8px;color:#333}

/* hero */
.hero{top:58px;height:181px;border-bottom:2px solid var(--orange)}
.hero-photo{position:absolute;inset:0;background:linear-gradient(100deg,#3a2418 0%,#6b4a35 35%,#b58e6d 55%,#8a6449 70%,#4b3124 100%)}
.hero-copy{position:absolute;left:15px;top:52px;width:190px;color:#fff}
.hero-copy .kicker{font-family:"Arimo",sans-serif;font-weight:700;font-size:13px;line-height:1}
.hero-copy h1{font-family:"Arimo",sans-serif;font-weight:700;font-size:21px;line-height:1.1;margin-top:2px}
.hero-copy p{font-size:7px;line-height:1.55;margin-top:4px}
.dots{position:absolute;left:284px;top:166px;display:flex;gap:2px}
.dots span{width:6px;height:6px;background:var(--orange);border:1px solid #fff}
.dots span:first-child{background:var(--red)}

/* identify */
.identify{top:241px;height:179px;background:var(--panel)}
.identify h2,.content h2{position:absolute;left:15px;top:14px;font-weight:400;font-size:15px}
.identify .sub{position:absolute;left:15px;top:34px;font-size:7.5px;color:#333}
.stat{position:absolute;top:66px;width:136px;font-size:8px}
.stat .label{padding-left:10px;text-transform:uppercase;color:#333;height:14px}
.stat .bar{margin-top:5px;height:16px;background:var(--bar-rest);display:flex}
.stat .fill{height:100%}
.stat .note{margin-top:8px;font-size:7.5px;line-height:1.9;color:#333}
.stat .note b{color:var(--red);font-weight:400;font-size:8.5px}

/* metrics */
.metrics{top:420px;height:180px;border-bottom:1px solid #ddd}
.metrics h2{position:absolute;left:15px;top:14px;font-weight:400;font-size:14.5px;text-transform:uppercase}
.metrics p{position:absolute;left:15px;width:400px;font-size:8.5px;line-height:1.8;color:#333}
.pie{position:absolute;left:439px;top:46px}
.legend{position:absolute;left:494px;top:58px;font-size:6px;color:#444;line-height:2}
.legend i{display:inline-block;width:7px;height:7px;margin-right:4px;vertical-align:-1px}
.trend{position:absolute;left:0;top:118px}

/* content */
.content{top:600px;height:179px;border-bottom:1px solid #ddd}
.content h2{top:22px}
.content p{position:absolute;left:15px;top:50px;width:320px;font-size:8.5px;line-height:1.8;color:#333}
.cta{position:absolute;left:15px;top:135px;width:98px;height:24px;background:var(--orange);color:#fff;font-size:8.5px;line-height:24px;text-align:center}
.content-photo{position:absolute;left:388px;top:32px;width:186px;height:124px;border:2px solid #555;background:linear-gradient(135deg,#5a3b2b 0%,#c48a6a 40%,#e8d7c7 70%,#3a3a3a 100%)}

/* link buttons */
.links{top:779px;height:62px;background:var(--panel)}
.link-btn{position:absolute;top:17px;height:30px;font-size:14px;line-height:30px;text-align:center}
.link-btn.packages{left:15px;width:279px;background:linear-gradient(90deg,var(--orange),var(--red));color:#fff}
.link-btn.articles{left:303px;width:283px;background:linear-gradient(90deg,#d9d9d9,#a9a9a9);color:#333}

/* newsletter */
.newsletter{top:841px;height:60px}
.news-bar{position:absolute;left:15px;top:12px;width:570px;height:36px;background:var(--orange-dark)}
.news-lead{position:absolute;left:0;top:0;width:290px;height:36px;background:linear-gradient(90deg,var(--orange),#f08a3a);display:flex;align-items:center;gap:12px;padding-left:12px;font-size:14px;color:#333}
.news-input{position:absolute;left:303px;top:10px;width:174px;height:16px;background:#fff;border:1px solid #f6b48a}
.news-btn{position:absolute;left:488px;top:10px;width:69px;height:16px;border:1px solid #fff;color:#fff;font-size:9px;line-height:14px;text-align:center}

/* footer */
.footer{top:901px;height:233px;background:var(--footer);color:#fff}
.strip{position:absolute;left:0;top:0;width:600px;height:46px;background:var(--footer-strip)}
.strip-item{position:absolute;top:16px;transform:translateX(-50%);color:var(--orange);font-size:10px;white-space:nowrap}
.notch{position:absolute;top:46px;width:0;height:0;border-left:8px solid transparent;border-right:8px solid transparent;border-top:7px solid var(--footer-strip);transform:translateX(-50%)}
.channel{position:absolute;top:58px;transform:translateX(-50%);text-align:center;font-size:10px}
.channel svg{display:block;margin:0 auto 5px}
.divider{position:absolute;left:15px;top:94px;width:570px;height:1px;background:#3a3a3a}
.fcol{position:absolute;top:108px;font-size:7px;line-height:1.9}
.fcol h3{font-weight:400;font-size:16px;margin-bottom:4px}
.fcol input{display:block;width:113px;height:13px;border:none;margin-top:6px;font-size:5px;padding-left:6px;font-family:inherit}
.fcol .send{margin-top:8px;width:34px;height:11px;background:var(--orange);font-size:5px;text-align:center;line-height:11px}
.social{position:absolute;left:182px;top:214px;display:flex;gap:7px}
.social span{width:7px;height:7px;border-radius:50%;background:#fff}
</style>
</head>
<body>
<div class="page">

  <div class="section topbar">
    <div class="phone">
      <svg width="6" height="7" viewBox="0 0 6 7"><path d="M1 0h1.5l.5 2-1 .7a4 4 0 0 0 1.5 2l.8-.8 1.7.6V6a1 1 0 0 1-1 1A5 5 0 0 1 0 1a1 1 0 0 1 1-1z" fill="#333"/></svg>
      0298 555 7310
    </div>
    <div class="chat">Click Here for Live Chat</div>
    <div class="login">Login</div>
  </div>

  <header class="section header">
    <div class="brand"><span class="brand-mark"></span><span class="brand-name">BRIGHT KETTLE MEDIA</span></div>
    <nav class="nav"><span>About</span><span>Strategic Planning</span><span>SEO</span><span>Packages</span><span>Articles</span><span>Contacts</span></nav>
  </header>

  <section class="section hero">
    <div class="hero-photo" role="img" aria-label="Close-up of a glossy desk surface with warm blurred light"></div>
    <div class="hero-copy">
      <div class="kicker">WHAT IS AN ONLINE</div>
      <h1>STRATEGIC PLAN?</h1>
      <p>An Online Strategic Plan is a lot like a business plan. You define look at your business, define your values, look at your competitors and think and talk to your customers to determine what you should do to improve your current situation.</p>
    </div>
    <div class="dots"><span></span><span></span><span></span><span></span></div>
  </section>

  <section class="section identify">
    <h2>Identify Your Customers</h2>
    <div class="sub">Do you REALLY know your customers?</div>
    <div class="stat" style="left:15px">
      <div class="label">Leave before 6 seconds</div>
      <div class="bar"><div class="fill" style="width:90%;background:var(--green)"></div></div>
      <div class="note" style="text-align:center">Unless finding what they want, <b>90%</b><br>of visitors will click off your page<br>within 6 seconds!</div>
    </div>
    <div class="stat" style="left:158px">
      <div class="label" style="padding-left:0">Seekwise users</div>
      <div class="bar"><div class="fill" style="width:33%;background:var(--red)"></div></div>
      <div class="note"><b>33%</b> use Seekwise+</div>
    </div>
    <div class="stat" style="left:303px">
      <div class="label" style="padding-left:0">Pagebook users</div>
      <div class="bar"><div class="fill" style="width:41%;background:var(--blue)"></div></div>
      <div class="note"><b>41%</b> prefer Pagebook</div>
    </div>
    <div class="stat" style="left:447px;width:139px">
      <div class="label" style="padding-left:0">Tablet users</div>
      <div class="bar"><div class="fill" style="width:31%;background:var(--sky)"></div></div>
      <div class="note"><b>31%</b> of all users are using a tablet</div>
    </div>
  </section>

  <section class="section metrics">
    <h2>Do you know your metrics?</h2>
    <p style="top:34px">Do you know what content is converting your visitors or worse, which content is driving them away!</p>
    <p style="top:88px">We work with you to develop strategies to identify this information, that allows you to optimise your content for your visitor’s preferences.</p>
    <svg class="pie" width="46" height="46" viewBox="0 0 46 46">
      <circle cx="23" cy="23" r="23" fill="#0a86c8"/>
      <path d="M23 23 L23 0 A23 23 0 0 1 45.2 17 Z" fill="var(--green)"/>
    </svg>
    <div class="legend">
      <div><i style="background:var(--green)"></i>69.63 % New Visitors</div>
      <div><i style="background:#0a86c8"></i>30.37% Returning Visitors</div>
    </div>
    <svg class="trend" width="600" height="60" viewBox="0 0 600 60">
      <polygon fill="#eef6fb" points="0,18 20,14 40,16 60,20 80,44 100,38 120,20 140,44 160,24 180,26 200,36 220,46 240,48 260,52 280,52 300,40 320,44 340,42 360,40 380,38 400,30 420,36 440,40 460,25 480,24 500,30 520,32 540,34 560,44 580,22 600,10 600,60 0,60"/>
      <polyline fill="none" stroke="var(--chart)" stroke-width="2" points="0,18 20,14 40,16 60,20 80,44 100,38 120,20 140,44 160,24 180,26 200,36 220,46 240,48 260,52 280,52 300,40 320,44 340,42 360,40 380,38 400,30 420,36 440,40 460,25 480,24 500,30 520,32 540,34 560,44 580,22 600,10"/>
      <g fill="var(--chart)">
        <circle cx="20" cy="14" r="2"/><circle cx="40" cy="16" r="2"/><circle cx="80" cy="44" r="2"/><circle cx="100" cy="38" r="2"/><circle cx="120" cy="20" r="2"/><circle cx="140" cy="44" r="2"/><circle cx="160" cy="24" r="2"/><circle cx="180" cy="26" r="2"/><circle cx="220" cy="46" r="2"/><circle cx="240" cy="48" r="2"/><circle cx="280" cy="52" r="2"/><circle cx="300" cy="40" r="2"/><circle cx="320" cy="44" r="2"/><circle cx="360" cy="40" r="2"/><circle cx="400" cy="30" r="2"/><circle cx="440" cy="40" r="2"/><circle cx="460" cy="25" r="2"/><circle cx="480" cy="24" r="2"/><circle cx="520" cy="32" r="2"/><circle cx="560" cy="44" r="2"/>
      </g>
    </svg>
  </section>

  <section class="section content">
    <h2>Create the Content that Sells</h2>
    <p>We work with you, provide the tools and support that will allow you to create content on a regular basis that will sell you business to your customers.</p>
    <div class="cta">What’s the Plan?</div>
    <div class="content-photo" role="img" aria-label="Hands typing on a computer keyboard"></div>
  </section>

  <section class="section links">
    <div class="link-btn packages">View Our Packages</div>
    <div class="link-btn articles">Strategic Planning Articles</div>
  </section>

  <section class="section newsletter">
    <div class="news-bar">
      <div class="news-lead">
        <svg width="20" height="14" viewBox="0 0 20 14"><rect width="20" height="14" fill="#fff"/><path d="M0 0 L10 8 L20 0" fill="none" stroke="var(--orange)" stroke-width="1.6"/></svg>
        Join our newsletter for exclusive deals
      </div>
      <div class="news-input"></div>
      <div class="news-btn">Subscribe</div>
    </div>
  </section>

  <footer class="section footer">
    <div class="strip">
      <div class="strip-item" style="left:76px">041 555 2870</div>
      <div class="strip-item" style="left:224px">Support - Sales</div>
      <div class="strip-item" style="left:375px">sales@brightkettlemedia.com.au</div>
      <div class="strip-item" style="left:526px">24x7x365</div>
    </div>
    <div class="notch" style="left:76px"></div>
    <div class="notch" style="left:224px"></div>
    <div class="notch" style="left:375px"></div>
    <div class="notch" style="left:526px"></div>

    <div class="channel" style="left:79px">
      <svg width="10" height="12" viewBox="0 0 6 7"><path d="M1 0h1.5l.5 2-1 .7a4 4 0 0 0 1.5 2l.8-.8 1.7.6V6a1 1 0 0 1-1 1A5 5 0 0 1 0 1a1 1 0 0 1 1-1z" fill="#fff"/></svg>
      Talk to you
    </div>
    <div class="channel" style="left:228px">
      <svg width="13" height="12" viewBox="0 0 13 12"><path d="M0 0h13v8H6l-3 3V8H0z" fill="#fff"/></svg>
      Live Chat
    </div>
    <div class="channel" style="left:375px">
      <svg width="14" height="10" viewBox="0 0 14 10"><rect width="14" height="10" fill="#fff"/><path d="M0 0 L7 6 L14 0" fill="none" stroke="var(--footer)" stroke-width="1.3"/></svg>
      Email Us
    </div>
    <div class="channel" style="left:527px">
      <svg width="13" height="12" viewBox="0 0 13 12"><path d="M0 5h3v7H0z M4 5 L7 0 h1 v4 h5 l-1.5 8 H4z" fill="#fff"/></svg>
      Good Support
    </div>
    <div class="divider"></div>

    <div class="fcol" style="left:26px">
      <h3>Quick Contact</h3>
      <div>Submit and our executives will<br>call you.</div>
      <input type="text" placeholder="Name">
      <input type="text" placeholder="E mail">
      <div class="send">Submit</div>
    </div>
    <div class="fcol" style="left:182px">
      <h3>Quick Links</h3>
      <div>About</div><div>SEO</div><div>Strategic Planning</div><div>Plans</div><div>Support</div>
    </div>
    <div class="fcol" style="left:299px">
      <h3>Support Links</h3>
      <div>Privacy Policy</div><div>Copyright</div><div>Legal</div><div>Disclosure</div><div>Terms &amp; Conditions</div>
    </div>
    <div class="fcol" style="left:446px">
      <h3>Contact Us</h3>
      <div>ADDRESS :</div>
      <div style="line-height:1.6">212 Kettle Road, Northgate,<br>Brisbane QLD 4013, Australia</div>
      <div style="margin-top:6px">TELEPHONE :</div>
      <div>+61 (7) 5550 1826</div>
    </div>

    <div class="social">
      <span></span><span></span><span></span><span></span><span></span><span></span><span></span><span></span><span></span><span></span><span></span><span></span>
    </div>
  </footer>

</div>
</body>
</html>
```